Robotic startup business cards

We are looking for a design for a set of business cards which reflect the spirit and humor of Vortalo Robotics. We want to present ourselves as sleek, professional, but laid-back consulting company.

We primarily focus on developing robotic arms software. This software controls robots and does things like grab items, pick objects up, move them, etc.

We want to allow you maximum design creativity, but do ask that you consider our existing style guidelines (see attached files) in order to make our brand cohesive.

Target Market(s)

Startups and Mid-size robotic companies

Industry/Entity Type

Business

Contact Information for Business Card

Miro Halvensky, PhD
Roboticist | Vortalo Consulting | 318.570.9164

Font styles to use
Other font styles liked:
• Source code pro

Requirements
Must have
• robots or robotic arms
• similar color scheme that works with existing brand guidelines
Nice to have
• please consider our existing style guidelines (see attached files) in order to make our brand cohesive.
• minimalism style is generally nice.
Should not have
• An old, boring, or corporate feel. Too much text.

```html
<!DOCTYPE html>
<html lang="en">
<head>
<meta charset="utf-8">
<title>Vortalo Robotics — Business Cards</title>
<link rel="stylesheet" href="https://fonts.googleapis.com/css2?family=Source+Code+Pro:wght@300;400;600;700&display=swap">
<style>
  :root {
    --backdrop: #e9e6e1;
    --card-black: #050505;
    --band-grey: #1b1b1b;
    --brand-green: #5ec39b;
    --ink-white: #f4f4f4;
  }
  * { box-sizing: border-box; margin: 0; padding: 0; }
  html, body {
    width: 1200px; height: 800px; overflow: hidden;
    background: var(--backdrop);
    font-family: "Source Code Pro", monospace;
  }
  .stage { position: relative; width: 1200px; height: 800px; }

  .card {
    position: absolute;
    width: 525px; height: 300px;
    background: var(--card-black);
    border-radius: 4px;
    box-shadow: 0 10px 28px rgba(0,0,0,.18);
    overflow: hidden;
  }

  /* Front */
  .card--front { left: 45px; top: 250px; }
  .front-lockup {
    position: absolute; left: 0; right: 0; top: 50%;
    transform: translateY(-50%);
    display: flex; align-items: center; justify-content: center; gap: 22px;
  }
  .front-lockup__dot {
    width: 34px; height: 34px; border-radius: 50%;
    background: var(--brand-green);
  }
  .front-lockup__name {
    color: var(--ink-white);
    font-weight: 300; font-size: 38px; letter-spacing: 10px;
  }

  /* Back */
  .card--back { left: 630px; top: 250px; }
  .back-stripe {
    position: absolute; left: 26px; top: 0; bottom: 0; width: 13px;
    background: var(--brand-green);
  }
  .back-band {
    position: absolute; left: 230px; top: 0; bottom: 0; width: 42px;
    background: var(--band-grey);
  }
  .back-email {
    position: absolute; left: 251px; top: 182px;
    transform: translate(-50%, -50%) rotate(-90deg);
    color: var(--brand-green);
    font-size: 12px; line-height: 1; white-space: nowrap;
  }
  .holder { position: absolute; left: 58px; top: 30px; }
  .holder__name {
    color: var(--ink-white); font-size: 20px; letter-spacing: .3px;
    font-weight: 300; white-space: nowrap; line-height: 1.2;
  }
  .holder__name strong { font-weight: 700; }
  .holder__degree { font-size: 15px; font-weight: 400; }
  .holder__role {
    color: var(--brand-green); font-size: 19px; font-weight: 400; line-height: 1.2;
  }
  .company {
    position: absolute; right: 26px; bottom: 26px; text-align: right;
  }
  .company__name {
    color: var(--ink-white); font-size: 17px; font-weight: 600; letter-spacing: .3px;
    white-space: nowrap;
  }
  .company__phone {
    color: var(--brand-green); font-size: 16px; margin-top: 8px; letter-spacing: .5px;
  }
</style>
</head>
<body>
<main class="stage">
  <section class="card card--front" aria-label="Card front">
    <div class="front-lockup">
      <span class="front-lockup__dot"></span>
      <span class="front-lockup__name">VORTALO</span>
    </div>
  </section>

  <section class="card card--back" aria-label="Card back">
    <div class="back-stripe"></div>
    <div class="back-band"></div>
    <p class="back-email">email@VortaloConsulting.com</p>
    <div class="holder">
      <p class="holder__name">MIRO<strong>HALVENSKY</strong>,<span class="holder__degree">PhD</span></p>
      <p class="holder__role">Roboticist</p>
    </div>
    <div class="company">
      <p class="company__name">VORTALO Consulting</p>
      <p class="company__phone">318.570.9164</p>
    </div>
  </section>
</main>
</body>
</html>
```